Nine Weeks and Nine Decades Book Cover Design

I need a book cover design for a book that I am writing, called "Nine Weeks and Nine Decades: The Climb and Descent of Reaching Lasting Momentum".

I have attached the Table of Contents and the first Introduction Chapter of the book, to provide more context on what the book is about.

The stories in the book primarily rely on my experience of running Skyvela Q, a long-haul low-cost airline. I use "sprint and marathon" because I'm a marathon runner and ironman triathlete, and its part of my identity.

I would love a design that captures a stylized combination of an aircraft taking off, and a person running. I have attached a photo of an Skyvela Q Norvane K640 aircraft (its different from Skyvela planes because of the "X" paint strokes on the tail of the plane. Ideally, if a stylized version of the X appears on the tail, that would be great, but without the "Skyvela" text.

Generally, the cover should convey "speed", and "curiosity".

Target Market(s)

Business Book Readers in Asia

Font styles to use
Sans Serif

Colors

Designer to choose colors to be used in the design.

Requirements
Must have
• Text in the Cover from the attached file
Nice to have
• Aircraft taking off and someone running
Should not have
• "Skyvela" name/text.

```html
<!DOCTYPE html>
<html lang="en">
<head>
<meta charset="utf-8">
<title>Nine Weeks and Nine Decades — Book Cover</title>
<link rel="stylesheet" href="https://fonts.googleapis.com/css2?family=Arimo:wght@400;700&display=swap">
<style>
  :root {
    --backdrop: #d9d9d9;
    --paper: #ffffff;
    --signal-red: #f21b1b;
    --title-white: #ffffff;
    --ink-grey: #555555;
    --spine-shade: #4a4a4a;
    --network-blue: #2a4fb0;
    --fuselage-grey: #b9bcc2;
    --runner-red: #7a1a14;
    --ribbon-blue: #4fb6e8;
  }
  * { margin: 0; padding: 0; box-sizing: border-box; }
  html, body {
    width: 1200px; height: 848px; overflow: hidden;
    background: var(--backdrop);
    font-family: "Arimo", Arial, Helvetica, sans-serif;
  }
  .cover {
    position: absolute; left: 322px; top: 24px;
    width: 556px; height: 800px;
    background: var(--paper);
    overflow: hidden;
  }
  .cover__hinge {
    position: absolute; left: 20px; top: 0; width: 3px; height: 100%;
    background: var(--spine-shade);
  }
  .art { position: absolute; }
  .art--network {
    left: 40px; top: 40px; width: 460px; height: 184px;
    background: radial-gradient(ellipse at 50% 50%, rgba(42,79,176,.28), rgba(42,79,176,.08) 65%, transparent 75%);
  }
  .art--aircraft {
    left: 198px; top: 99px; width: 250px; height: 198px;
    background: linear-gradient(150deg, var(--fuselage-grey), #e6e7ea 55%, #8a1f1f);
    border-radius: 40% 20% 40% 30%;
    opacity: .85;
  }
  .art--ribbons {
    left: 66px; top: 428px; width: 356px; height: 284px;
    background: linear-gradient(110deg, rgba(79,182,232,.35), rgba(242,27,27,.25) 50%, rgba(79,182,232,.3));
    border-radius: 50% 30% 50% 40%;
  }
  .art--runner {
    left: 277px; top: 474px; width: 237px; height: 264px;
    background: linear-gradient(160deg, #1e3a6a, var(--runner-red) 35%, #3a0d0a);
    border-radius: 45% 35% 30% 40%;
    opacity: .9;
  }
  .title { position: absolute; left: 22px; top: 221px; width: 478px; }
  .title__line {
    display: block; height: 49px; line-height: 49px;
    padding-left: 16px;
    font-size: 40px; font-weight: 400; letter-spacing: .5px;
    color: var(--title-white);
  }
  .title__line--band {
    background: var(--signal-red);
    box-shadow: 0 4px 8px rgba(242,27,27,.35);
  }
  .title__line--joiner {
    color: var(--signal-red); height: 56px; line-height: 60px;
    padding-left: 20px;
    background: var(--paper);
  }
  .subtitle {
    position: absolute; left: 26px; top: 386px;
    font-size: 14.5px; font-weight: 700; color: var(--ink-grey);
  }
  .author {
    position: absolute; left: 79px; top: 685px; width: 477px; height: 53px;
    background: var(--signal-red);
    color: var(--title-white);
    font-size: 27px; font-weight: 700; letter-spacing: .5px;
    line-height: 53px; text-align: right; padding-right: 16px;
  }
  .blurb {
    position: absolute; left: 20px; top: 745px; width: 536px;
    font-size: 12.4px; font-weight: 700; line-height: 15.5px;
    color: var(--ink-grey); text-align: center;
  }
</style>
</head>
<body>
  <main class="cover">
    <div class="cover__hinge"></div>
    <div class="art art--network" role="img" aria-label="Dotted world map with connected network lines"></div>
    <div class="art art--aircraft" role="img" aria-label="Wide-body aircraft taking off, tail marked with painted strokes"></div>
    <h1 class="title">
      <span class="title__line title__line--band">NINE WEEKS</span>
      <span class="title__line title__line--joiner">AND</span>
      <span class="title__line title__line--band">NINE DECADES</span>
    </h1>
    <p class="subtitle">The Climb and Descent of Reaching Lasting Momentum</p>
    <div class="art art--ribbons" role="img" aria-label="Flowing red and blue speed ribbons"></div>
    <div class="art art--runner" role="img" aria-label="Silhouette of a sprinting runner"></div>
    <p class="author">DARIN KESTEL-HADI</p>
    <p class="blurb">A startup CEO shares his experiences of building innovative business<br>with Curiosity and Purpose as core guiding principles to create an<br>enterpreneurial culture and archieve breakthrough results</p>
  </main>
</body>
</html>
```